Book cover for book about Climate Change

Looking for a clean, bold, and attractive cover for a mass-market paperback (5.5"x 8.5") about solving the climate change problem. Title is either "When Rivers Learn to Sing” or A Lantern Over Quiet Fields” (your choice), subtitle is "A five-step plan to reverse climate change — to ensure that your grandchildren will live on a clean and comfortable planet," author is Dale Pruitt. Thinking that it *might* feature an image of Earth (or a portion thereof) and its very thin layer of atmosphere -- but STRONGLY encourage other ideas too!

Requirements
Nice to have
• Keep it positive — NOT scary doom-and-gloom

```html
<!DOCTYPE html>
<html lang="en">
<head>
<meta charset="utf-8">
<title>A Lantern Over Quiet Fields — Book Cover</title>
<link rel="stylesheet" href="https://fonts.googleapis.com/css2?family=Archivo+Black&family=Montserrat:wght@300;400&display=swap">
<style>
  :root {
    --backdrop: #e9e7e3;
    --sky-top: #d9d2c8;
    --sky-mid: #d8b690;
    --haze: #b99a7c;
    --field: #a07a3c;
    --field-deep: #6f5a2c;
    --mist-light: #c9c9c9;
    --mist-dark: #2b2b2b;
    --stripe-red: #f5080b;
    --stripe-grey: #7c7a7b;
    --title-fill: #e6ebe2;
    --title-edge: #1f5a2c;
    --accent-red: #e00d0d;
    --type-white: #ffffff;
    --ground-green: #3cc13b;
  }
  html, body {
    margin: 0;
    width: 1200px;
    height: 1200px;
    overflow: hidden;
    background: var(--backdrop);
  }
  .stage {
    position: relative;
    width: 1200px;
    height: 1200px;
  }
  .book-cover {
    position: absolute;
    left: 234px;
    top: 20px;
    width: 731px;
    height: 1160px;
    box-shadow: 0 10px 30px rgba(0,0,0,0.18);
  }
  .title-main {
    font-family: "Archivo Black", "Arial Black", sans-serif;
    fill: var(--title-fill);
    stroke: var(--title-edge);
    stroke-width: 3;
    paint-order: stroke;
  }
  .title-link {
    font-family: "Archivo Black", "Arial Black", sans-serif;
    font-size: 58px;
  }
  .title-link--white { fill: var(--type-white); }
  .title-link--red { fill: var(--accent-red); }
  .subtitle {
    font-family: "Montserrat", sans-serif;
    font-weight: 400;
    font-size: 15.5px;
    fill: var(--type-white);
    letter-spacing: 0.3px;
  }
  .byline-label {
    font-family: "Montserrat", sans-serif;
    font-weight: 400;
    font-size: 14px;
    fill: var(--type-white);
    letter-spacing: 2px;
  }
  .author-name {
    font-family: "Montserrat", sans-serif;
    font-weight: 300;
    font-size: 44px;
    fill: var(--type-white);
    letter-spacing: 1px;
  }
</style>
</head>
<body>
<main class="stage">
  <svg class="book-cover" viewBox="0 0 731 1160" xmlns="http://www.w3.org/2000/svg">
    <defs>
      <linearGradient id="warm-landscape" x1="0" y1="0" x2="0" y2="1">
        <stop offset="0" stop-color="var(--sky-top)"/>
        <stop offset="0.38" stop-color="var(--sky-mid)"/>
        <stop offset="0.6" stop-color="var(--haze)"/>
        <stop offset="0.8" stop-color="var(--field)"/>
        <stop offset="1" stop-color="var(--field-deep)"/>
      </linearGradient>
      <linearGradient id="misty-ridges" x1="0" y1="0" x2="0" y2="1">
        <stop offset="0" stop-color="var(--mist-light)"/>
        <stop offset="0.45" stop-color="var(--mist-dark)"/>
        <stop offset="0.8" stop-color="#5a5a5a"/>
        <stop offset="1" stop-color="#9a9a9a"/>
      </linearGradient>
      <filter id="title-glow" x="-10%" y="-20%" width="120%" height="140%">
        <feDropShadow dx="0" dy="0" stdDeviation="4" flood-color="#1f5a2c" flood-opacity="0.7"/>
      </filter>
    </defs>

    <rect class="photo-lower" x="0" y="660" width="731" height="474" fill="url(#misty-ridges)"
          role="img" aria-label="Black and white photo of misty mountain ridges with a lone hiker standing in the fog"/>
    <polygon class="photo-upper" points="0,0 731,0 731,852 0,666" fill="url(#warm-landscape)"
             role="img" aria-label="Photo of golden grassland and hazy mountains under a warm sunrise sky"/>

    <polygon class="stripe stripe--grey" points="0,666 731,852 731,912 0,723" fill="var(--stripe-grey)"/>
    <polygon class="stripe stripe--red" points="0,600 731,774 731,843 0,654" fill="var(--stripe-red)"/>

    <g class="title" filter="url(#title-glow)">
      <text class="title-main" x="86" y="318" font-size="130">A</text>
      <text class="title-main" x="86" y="444" font-size="122" textLength="560" lengthAdjust="spacingAndGlyphs">LANTERN</text>
    </g>
    <text x="86" y="512" textLength="560" lengthAdjust="spacingAndGlyphs">
      <tspan class="title-link title-link--white">Over </tspan><tspan class="title-link title-link--red">Quiet Fields</tspan>
    </text>

    <text class="subtitle" x="365" y="580" text-anchor="middle">A five-step plan to reverse climate change —</text>
    <text class="subtitle" x="365" y="604" text-anchor="middle">to ensure that your grandchildren will live on a clean and comfortable planet.</text>

    <text class="byline-label" x="345" y="1006" text-anchor="middle">BY :</text>
    <text class="author-name" x="341" y="1064" text-anchor="middle">DALE PRUITT</text>

    <rect class="ground-band" x="0" y="1134" width="731" height="26" fill="var(--ground-green)"/>
  </svg>
</main>
</body>
</html>
```